Animated GIF banner for mobile app

We need a GIF Banner designed that alternates between two different ads.

Details are;
Pixel Size (W X H) 300 X 250
Minimum DPI 72dpi
File Size 40kb
File Size (Rich Media) 150kb

Ad 1 Text:
Lost super? More than one super fund? Contact us

Ad 2 Text:
Time to review your home loan? Contact us

Target Market(s)

30-55 year olds

Industry/Entity Type

Financial Service

Font styles to use
Sans Serif

Colors
0555a3
3176b5
85abd2

```html
<!DOCTYPE html>
<html lang="en">
<head>
<meta charset="utf-8">
<title>Financial Services Banner Set</title>
<link rel="stylesheet" href="https://fonts.googleapis.com/css2?family=Montserrat:wght@700;800;900&display=swap">
<style>
  :root {
    --canvas-bg: #efefef;
    --lime: #84c71a;
    --white: #ffffff;
    --button-text: #4a4a4a;
    --brand-blue: #0555a3;
    --chalk-dark: #1c1c24;
    --chalk-mid: #2b2b35;
    --warm-dark: #1a1210;
    --warm-mid: #3a2a20;
    --photo-cool: #4a3f4e;
    --photo-warm: #6a4636;
  }
  * { box-sizing: border-box; margin: 0; padding: 0; }
  html, body {
    width: 1200px; height: 1200px; overflow: hidden;
    background: var(--canvas-bg);
    font-family: "Montserrat", Arial, sans-serif;
  }
  .banner {
    position: absolute; left: 293px;
    width: 615px; height: 512px; overflow: hidden;
  }
  .banner--super { top: 66px;
    background: radial-gradient(circle at 40% 40%, var(--chalk-mid), var(--chalk-dark) 75%); }
  .banner--loan { top: 658px;
    background: radial-gradient(circle at 60% 35%, var(--warm-mid), var(--warm-dark) 70%); }

  .photo { position: absolute; }
  .photo--piggy {
    left: 380px; top: 230px; width: 235px; height: 282px;
    background: linear-gradient(160deg, var(--chalk-mid) 0%, var(--photo-cool) 100%);
  }
  .photo--house {
    left: 380px; top: 250px; width: 235px; height: 262px;
    background: linear-gradient(160deg, var(--warm-mid) 0%, var(--photo-warm) 100%);
  }

  .brand-box {
    position: absolute; left: 434px; top: 0; width: 146px; height: 128px;
    background: var(--white);
    display: flex; flex-direction: column; align-items: center; justify-content: center; gap: 8px;
    text-align: center;
  }
  .brand-box__mark { width: 22px; height: 22px; border-radius: 50%; background: var(--brand-blue); }
  .brand-box__name {
    color: var(--brand-blue); font-weight: 700; font-size: 14px; line-height: 1.15;
  }

  .headline { position: absolute; left: 80px; top: 76px; text-transform: uppercase; }
  .headline__big {
    display: block; color: var(--lime); font-weight: 900;
    font-size: 88px; line-height: 74px; letter-spacing: -3px;
  }
  .headline__small {
    display: block; color: var(--white); font-weight: 900;
    font-size: 44px; line-height: 46px; letter-spacing: -1px;
  }
  .banner--super .headline__small:first-of-type { margin-top: 8px; }
  .banner--loan .headline { top: 72px; }
  .banner--loan .headline__big { letter-spacing: -4px; }
  .banner--loan .headline__big:first-of-type { margin-top: 6px; }

  .cta {
    position: absolute; left: 80px; top: 382px; height: 56px; width: 247px;
    display: flex; border-radius: 3px; overflow: hidden;
    box-shadow: 0 3px 0 rgba(0,0,0,0.35);
  }
  .cta__label {
    flex: 0 0 186px; background: var(--white); color: var(--button-text);
    font-weight: 800; font-size: 19px;
    display: flex; align-items: center; justify-content: center;
  }
  .cta__arrow {
    flex: 1; background: var(--lime);
    display: flex; align-items: center; justify-content: center;
  }
</style>
</head>
<body>

  <section class="banner banner--super">
    <div class="photo photo--piggy" role="img" aria-label="Photo: piggy bank wearing glasses on a stack of books"></div>
    <div class="brand-box">
      <span class="brand-box__mark"></span>
      <span class="brand-box__name">Harlow Bennett<br>Financial Solutions</span>
    </div>
    <h1 class="headline">
      <span class="headline__big">Lost</span>
      <span class="headline__big">Super?</span>
      <span class="headline__small">More than</span>
      <span class="headline__small">one super</span>
      <span class="headline__small">fund?</span>
    </h1>
    <a class="cta">
      <span class="cta__label">CONTACT US</span>
      <span class="cta__arrow">
        <svg width="30" height="26" viewBox="0 0 30 26" aria-hidden="true">
          <path d="M3 3 L13 13 L3 23 M15 3 L25 13 L15 23" fill="none" stroke="#1a1a1a" stroke-width="5" stroke-linecap="round" stroke-linejoin="round"/>
        </svg>
      </span>
    </a>
  </section>

  <section class="banner banner--loan">
    <div class="photo photo--house" role="img" aria-label="Photo: small wooden house model tied with a ribbon"></div>
    <div class="brand-box">
      <span class="brand-box__mark"></span>
      <span class="brand-box__name">Harlow Bennett<br>Financial Solutions</span>
    </div>
    <h1 class="headline">
      <span class="headline__small">Time to</span>
      <span class="headline__small">review</span>
      <span class="headline__small">your</span>
      <span class="headline__big">Home</span>
      <span class="headline__big">Loan?</span>
    </h1>
    <a class="cta">
      <span class="cta__label">CONTACT US</span>
      <span class="cta__arrow">
        <svg width="30" height="26" viewBox="0 0 30 26" aria-hidden="true">
          <path d="M3 3 L13 13 L3 23 M15 3 L25 13 L15 23" fill="none" stroke="#1a1a1a" stroke-width="5" stroke-linecap="round" stroke-linejoin="round"/>
        </svg>
      </span>
    </a>
  </section>

</body>
</html>
```